Business Card Design

WE are looking for a premium quality Business Cards for a Law Firm . Copies of our current business card is attached.
Updates

Went on vacation/holiday

Contact Information for Business Card

xyz

```html
<!DOCTYPE html>
<html lang="en">
<head>
<meta charset="utf-8">
<title>Harrow Lawyers – Business Card</title>
<link rel="stylesheet" href="https://fonts.googleapis.com/css2?family=Lato:ital,wght@0,400;0,700;0,900;1,400&display=swap">
<style>
  :root {
    --backdrop: #2a2c30;
    --firm-green: #0d2a1e;
    --gold: #d9a45c;
    --ink: #1c1f1d;
    --muted: #4a4f4c;
    --paper: #ffffff;
    --rule: #1c1f1d;
  }
  * { margin: 0; padding: 0; box-sizing: border-box; }
  html, body {
    width: 1200px; height: 952px; overflow: hidden;
    background: var(--backdrop);
    font-family: "Lato", sans-serif;
  }
  .canvas { position: relative; width: 1200px; height: 952px; }

  .card {
    position: absolute;
    width: 560px; height: 320px;
    border-radius: 24px;
    overflow: hidden;
    box-shadow: 0 18px 40px rgba(0,0,0,0.45);
  }

  /* Front: contact side */
  .card--front { left: 580px; top: 110px; background: var(--paper); }
  .front__brand {
    position: absolute; left: 0; top: 0; width: 260px; height: 100%;
    display: flex; flex-direction: column; align-items: center; justify-content: center; gap: 14px;
  }
  .brand-circle {
    width: 58px; height: 58px; border-radius: 50%;
    border: 3px solid var(--gold);
  }
  .brand-name {
    font-weight: 900; color: var(--firm-green);
    font-size: 26px; letter-spacing: 3px; text-transform: uppercase;
    text-align: center; line-height: 1.15;
  }
  .brand-name span { display: block; font-size: 13px; letter-spacing: 9px; }

  .front__divider {
    position: absolute; left: 268px; top: 0; width: 1.5px; height: 100%;
    background: var(--rule);
  }
  .person-badge {
    position: absolute; left: 252px; top: 92px; width: 34px; height: 34px;
    background: var(--paper); border: 1.5px solid var(--rule); border-radius: 9px;
    display: flex; align-items: center; justify-content: center;
  }
  .contact-tab {
    position: absolute; left: 244px; top: 168px; width: 24px; height: 92px;
    background: var(--firm-green); border-radius: 8px 0 0 8px;
    display: flex; flex-direction: column; align-items: center; justify-content: space-evenly;
  }

  .front__details { position: absolute; left: 294px; top: 90px; right: 20px; color: var(--ink); }
  .holder-name { font-weight: 900; font-size: 25px; letter-spacing: 0.5px; text-transform: uppercase; line-height: 1; }
  .holder-title { font-size: 10px; font-weight: 700; text-transform: uppercase; letter-spacing: 0.4px; margin-top: 5px; }
  .holder-quals { font-size: 10px; font-style: italic; color: var(--muted); margin-top: 2px; }
  .address { display: flex; gap: 7px; margin-top: 14px; font-size: 12px; line-height: 1.3; }
  .contact-list { list-style: none; margin-top: 12px; font-size: 12.5px; line-height: 1.62; }

  /* Back: brand side */
  .card--back { left: 60px; top: 520px; background: var(--firm-green); }
  .back__name {
    position: absolute; left: 48px; top: 52px;
    font-weight: 900; color: var(--gold);
    font-size: 34px; letter-spacing: 4px; text-transform: uppercase; line-height: 1.1;
  }
  .back__name span { display: block; font-size: 15px; letter-spacing: 12px; }
  .back__ring {
    position: absolute; left: 250px; top: 120px; width: 360px; height: 360px;
    border-radius: 50%; border: 8px solid var(--gold);
  }
</style>
</head>
<body>
<main class="canvas">

  <section class="card card--front" aria-label="Business card front">
    <div class="front__brand">
      <div class="brand-circle" aria-hidden="true"></div>
      <div class="brand-name">Harrow<span>Lawyers</span></div>
    </div>

    <div class="front__divider"></div>

    <div class="person-badge" aria-hidden="true">
      <svg width="18" height="18" viewBox="0 0 18 18"><rect width="18" height="18" rx="3" fill="#d9a45c"/><circle cx="9" cy="7" r="3.2" fill="#fff"/><path d="M3.5 16c0-3.2 2.5-5 5.5-5s5.5 1.8 5.5 5z" fill="#fff"/></svg>
    </div>

    <div class="contact-tab" aria-hidden="true">
      <svg width="12" height="12" viewBox="0 0 12 12"><path d="M3 1l2 2.5-1.2 1.2a7 7 0 0 0 3.5 3.5L8.5 7 11 9l-1.5 2C5 11 1 7 1 2.5z" fill="#d9a45c"/></svg>
      <svg width="12" height="12" viewBox="0 0 12 12"><rect x="3" y="1" width="6" height="10" rx="1.2" fill="#d9a45c"/><circle cx="6" cy="9.3" r="0.8" fill="#0d2a1e"/></svg>
      <svg width="12" height="12" viewBox="0 0 12 12"><rect x="1" y="2.5" width="10" height="7" rx="1" fill="#d9a45c"/><path d="M1.5 3l4.5 3.5L10.5 3" stroke="#0d2a1e" stroke-width="1" fill="none"/></svg>
      <svg width="12" height="12" viewBox="0 0 12 12"><path d="M2 2l8 3.5-3.2 1.3L5.5 10z" fill="#d9a45c"/></svg>
    </div>

    <div class="front__details">
      <h1 class="holder-name">Daniel Morrow</h1>
      <p class="holder-title">Director &amp; Principal Solicitor</p>
      <p class="holder-quals">MBA, Juris Doctor</p>
      <div class="address">
        <svg width="14" height="14" viewBox="0 0 14 14" aria-hidden="true"><rect width="14" height="14" rx="3" fill="#d9a45c"/><path d="M7 3a2.6 2.6 0 0 0-2.6 2.6C4.4 7.8 7 11 7 11s2.6-3.2 2.6-5.4A2.6 2.6 0 0 0 7 3z" fill="#fff"/><circle cx="7" cy="5.6" r="1" fill="#d9a45c"/></svg>
        <p>Level 3, Harrow House, 42 Ellery Terrace,<br>Kelvin Grove, QLD 4059</p>
      </div>
      <ul class="contact-list">
        <li>+61 7 3000 1234</li>
        <li>+61 0400 111 222</li>
        <li>daniel@harrowlawyers.com.au</li>
        <li>www.harrowlawyers.com.au</li>
      </ul>
    </div>
  </section>

  <section class="card card--back" aria-label="Business card back">
    <div class="back__name">Harrow<span>Lawyers</span></div>
    <div class="back__ring" aria-hidden="true"></div>
  </section>

</main>
</body>
</html>
```